Aerospace Center needs app design

We need a design that would be a creative and innovative look of a simple idea connecting air traffic control situations with sonification.
We would like to see designs that use the elements shown in the short video which are different pads, showing 4 different colors, connecting with a degree and feeling of urgency. The different pads will be movable over screen, similar as to a whiteboard where you can move things around. Each of those pads has 4 different elements that are shown:
- ATC Event (you can chose different setups)
- Select a status (you can chose between Information, Caution and Alert. Color needs to feel more alert from Information to Alert.
- Notes box (you can open the box and write additional text on it)
- Music (you can chose different files. on the right side you can see a small group of notes. When you hover over the notes, music will be played without pressing a play or stop button.
The second video is an overview of music archival program that is connected with the pads.
Look and feel
Each slider illustrates characteristics of the customer's brand and the style your logo design should communicate.

```html
<!DOCTYPE html>
<html lang="en">
<head>
<meta charset="utf-8">
<title>ATC Sonification Pads – States</title>
<link rel="stylesheet" href="https://fonts.googleapis.com/css2?family=Arimo:wght@400;700&display=swap">
<style>
  :root{
    --ink:#000;
    --white:#fff;
    --blue-pad:#003399;
    --blue-btn-top:#00aaea;
    --blue-btn-bot:#0098dd;
    --green-pad:#06ad06;
    --green-btn-top:#4fd400;
    --green-btn-bot:#80ec00;
    --green-hover-top:#a9e3a9;
    --green-hover-bot:#eefaee;
    --green-select:#8ff500;
    --green-dim-text:#2fc22f;
    --orange-pad:#ff6600;
    --orange-btn-top:#ff9f00;
    --orange-btn-bot:#ffb800;
    --orange-dim-text:#ff7c00;
    --yellow-select:#ffff00;
    --red-pad:#ff0000;
    --red-btn-top:#900000;
    --red-btn-bot:#660000;
    --red-dim-text:#e80000;
    --red-select:#ffdede;
    --library-border:#8bdc8b;
    --library-text:#8a8a8a;
  }
  *{box-sizing:border-box;margin:0;padding:0}
  html,body{width:1200px;height:1200px;overflow:hidden;background:#fff}
  body{font-family:"Arimo",Arial,sans-serif;position:relative}
  .stage{position:absolute;left:0;top:0;width:1932px;height:1932px;transform:scale(.62112);transform-origin:0 0}

  .state-label{position:absolute;font-weight:400;font-size:52px;line-height:60px;text-align:center;color:var(--ink)}

  .pad{position:absolute;width:552px;height:492px;border-radius:34px;background:var(--pad-bg)}
  .pad::before{content:"";position:absolute;inset:10px;border:4px solid var(--white);border-radius:26px}
  .pad--blue{--pad-bg:var(--blue-pad);--btn-top:var(--blue-btn-top);--btn-bot:var(--blue-btn-bot);--head:var(--ink)}
  .pad--green{--pad-bg:var(--green-pad);--btn-top:var(--green-btn-top);--btn-bot:var(--green-btn-bot);--head:var(--ink)}
  .pad--green-active{--pad-bg:var(--green-pad);--btn-top:var(--green-btn-top);--btn-bot:var(--green-btn-bot);--head:var(--white)}
  .pad--orange{--pad-bg:var(--orange-pad);--btn-top:var(--orange-btn-top);--btn-bot:var(--orange-btn-bot);--head:var(--white)}
  .pad--red{--pad-bg:var(--red-pad);--btn-top:var(--red-btn-top);--btn-bot:var(--red-btn-bot);--head:var(--white)}

  .pad-id{position:absolute;left:40px;top:20px;font-weight:700;font-size:54px;line-height:60px;color:var(--head)}
  .pad-close{position:absolute;left:484px;top:30px;width:38px;height:38px}
  .pad-close path{stroke:var(--head)}
  .col-head{position:absolute;top:118px;width:247px;text-align:center;font-weight:700;font-size:33px;line-height:44px;color:var(--head)}
  .col-head--status{left:14px}
  .col-head--event{left:279px}

  .pad-btn{position:absolute;border-radius:13px;background:linear-gradient(var(--btn-top),var(--btn-bot));
    display:flex;align-items:center;padding-left:30px;font-weight:700;font-size:33px;color:var(--ink);white-space:nowrap}
  .pad-btn.col-status{left:25px;width:247px}
  .pad-btn.col-event{left:282px;width:247px}
  .pad-btn.track{left:282px;width:164px}
  .pad-btn.notes{align-items:flex-start;padding-top:8px}
  .pad-btn.music{left:452px;width:77px;padding:0;justify-content:center}
  .pad-btn.small{font-size:25px}
  .pad-btn.track.small{font-size:25px}
  .pad-btn.dim{color:var(--dim)}

  .pad--green .pad-btn.hovered{background:linear-gradient(var(--green-hover-top),var(--green-hover-bot));font-size:40px;padding-left:19px}
  .pad--green-active .pad-btn.selected{background:var(--green-select);font-size:40px;padding-left:19px}
  .pad--green-active{--dim:var(--green-dim-text)}
  .pad--orange{--dim:var(--orange-dim-text)}
  .pad--orange .pad-btn.selected{background:var(--yellow-select);font-size:52px}
  .pad--orange .pad-btn.selected.col-event{font-size:38px}
  .pad--red{--dim:var(--red-dim-text)}
  .pad--red .pad-btn.selected{background:var(--red-select);color:var(--red-dim-text);font-size:52px;padding-left:56px}
  .pad--red .pad-btn.selected.col-event{font-size:38px;padding-left:28px}
  .pad--red .pad-btn.notes,.pad--red .pad-btn.track{color:#2a0000}
  .pad--red .pad-btn.notes{color:#2a0000}

  .music-icon{width:66px;height:52px}
  .pointer{position:absolute;width:36px;height:36px}
  .sound-waves{position:absolute;left:926px;top:1062px;width:96px;height:108px}

  .library-popup{position:absolute;left:682px;top:1723px;width:247px;height:120px;background:var(--white);
    border:5px solid var(--library-border);border-radius:10px;display:flex;align-items:center;justify-content:center;
    font-weight:700;font-size:25px;color:var(--library-text);letter-spacing:.5px}
</style>
</head>
<body>
<svg width="0" height="0" style="position:absolute">
  <defs>
    <symbol id="icon-staff" viewBox="0 0 66 52">
      <g stroke="#000" stroke-width="3">
        <line x1="2" y1="8" x2="64" y2="8"/>
        <line x1="2" y1="18" x2="64" y2="18"/>
        <line x1="2" y1="28" x2="64" y2="28"/>
        <line x1="2" y1="38" x2="64" y2="38"/>
        <line x1="2" y1="48" x2="64" y2="48"/>
        <line x1="36" y1="40" x2="36" y2="2"/>
      </g>
      <ellipse cx="28" cy="41" rx="9" ry="6.5" fill="#000" transform="rotate(-20 28 41)"/>
      <path d="M36 2 C40 10 48 12 46 24 C45 16 40 14 36 13 Z" fill="#000"/>
    </symbol>
    <symbol id="icon-pointer" viewBox="0 0 32 32">
      <path d="M2 2 L22 8 L15.5 13 L29 26.5 L25.5 30 L12 16.5 L7 23 Z" fill="#000"/>
    </symbol>
    <symbol id="icon-close" viewBox="0 0 38 38">
      <path d="M6 6 L32 32 M32 6 L6 32" stroke-width="8" stroke-linecap="round" fill="none"/>
    </symbol>
  </defs>
</svg>

<main class="stage">
  <div class="state-label" style="left:100px;top:850px;width:280px">on mouse<br>over</div>
  <div class="state-label" style="left:160px;top:1474px;width:210px">on click</div>

  <!-- Idle pad -->
  <section class="pad pad--blue" style="left:400px;top:150px">
    <div class="pad-id">AB1</div>
    <svg class="pad-close"><use href="#icon-close"/></svg>
    <div class="col-head col-head--status">Status</div>
    <div class="col-head col-head--event">ATC Event</div>
    <div class="pad-btn col-status" style="top:173px;height:62px">Information</div>
    <div class="pad-btn col-status" style="top:240px;height:62px">Caution</div>
    <div class="pad-btn col-status" style="top:307px;height:62px">Alert</div>
    <div class="pad-btn col-status notes" style="top:378px;height:89px">Notes</div>
    <div class="pad-btn col-event" style="top:173px;height:62px">Landing</div>
    <div class="pad-btn col-event" style="top:240px;height:62px">Departure</div>
    <div class="pad-btn col-event" style="top:307px;height:62px">Moon</div>
    <div class="pad-btn track" style="top:378px;height:89px"></div>
    <div class="pad-btn music" style="top:378px;height:89px"><svg class="music-icon"><use href="#icon-staff"/></svg></div>
  </section>

  <!-- Hover pad -->
  <section class="pad pad--green" style="left:400px;top:705px">
    <div class="pad-id">AB1</div>
    <svg class="pad-close"><use href="#icon-close"/></svg>
    <div class="col-head col-head--status">Status</div>
    <div class="col-head col-head--event">ATC Event</div>
    <div class="pad-btn col-status hovered" style="top:175px;height:92px">Information</div>
    <div class="pad-btn col-status small" style="top:273px;height:44px">Caution</div>
    <div class="pad-btn col-status small" style="top:325px;height:44px">Alert</div>
    <div class="pad-btn col-status notes" style="top:379px;height:88px">Notes</div>
    <div class="pad-btn col-event small" style="top:175px;height:45px">Landing</div>
    <div class="pad-btn col-event hovered" style="top:225px;height:93px;padding-left:28px;font-size:38px">Departure</div>
    <div class="pad-btn col-event small" style="top:325px;height:44px">Moon</div>
    <div class="pad-btn track small" style="top:379px;height:88px">Aria....</div>
    <div class="pad-btn music" style="top:379px;height:88px"><svg class="music-icon"><use href="#icon-staff"/></svg></div>
  </section>
  <svg class="sound-waves" viewBox="0 0 96 108" aria-hidden="true">
    <g fill="none" stroke="#000" stroke-width="8" stroke-linecap="butt">
      <path d="M14 62 A14 14 0 0 1 24 72"/>
      <path d="M14 38 A38 38 0 0 1 46 88"/>
      <path d="M4 10 A70 70 0 0 1 80 98"/>
    </g>
  </svg>
  <svg class="pointer" style="left:608px;top:944px"><use href="#icon-pointer"/></svg>
  <svg class="pointer" style="left:877px;top:994px"><use href="#icon-pointer"/></svg>
  <svg class="pointer" style="left:798px;top:1117px"><use href="#icon-pointer"/></svg>

  <!-- Caution pad -->
  <section class="pad pad--orange" style="left:1058px;top:715px">
    <div class="pad-id">AB1</div>
    <svg class="pad-close"><use href="#icon-close"/></svg>
    <div class="col-head col-head--status">Status</div>
    <div class="col-head col-head--event">ATC Event</div>
    <div class="pad-btn col-status small dim" style="top:173px;height:47px">Information</div>
    <div class="pad-btn col-status selected" style="top:225px;height:92px">Caution</div>
    <div class="pad-btn col-status small dim" style="top:323px;height:46px">Alert</div>
    <div class="pad-btn col-status notes" style="top:378px;height:88px">Notes</div>
    <div class="pad-btn col-event small dim" style="top:173px;height:47px">landing</div>
    <div class="pad-btn col-event selected" style="top:225px;height:92px">Departure</div>
    <div class="pad-btn col-event small dim" style="top:323px;height:46px">Moon</div>
    <div class="pad-btn track small" style="top:378px;height:88px">Aria....</div>
    <div class="pad-btn music" style="top:378px;height:88px"><svg class="music-icon"><use href="#icon-staff"/></svg></div>
  </section>

  <!-- Click pad -->
  <section class="pad pad--green-active" style="left:400px;top:1255px">
    <div class="pad-id">AB1</div>
    <svg class="pad-close"><use href="#icon-close"/></svg>
    <div class="col-head col-head--status">Status</div>
    <div class="col-head col-head--event">ATC Event</div>
    <div class="pad-btn col-status selected" style="top:175px;height:92px">Information</div>
    <div class="pad-btn col-status small dim" style="top:272px;height:45px">Caution</div>
    <div class="pad-btn col-status small dim" style="top:325px;height:45px">Alert</div>
    <div class="pad-btn col-status notes" style="top:380px;height:87px">Notes</div>
    <div class="pad-btn col-event small dim" style="top:175px;height:45px">Landing</div>
    <div class="pad-btn col-event selected" style="top:225px;height:93px;padding-left:28px;font-size:38px">Departure</div>
    <div class="pad-btn col-event small dim" style="top:325px;height:45px">Moon</div>
    <div class="pad-btn track small" style="top:380px;height:87px">Aria....</div>
    <div class="pad-btn music" style="top:380px;height:87px"><svg class="music-icon"><use href="#icon-staff"/></svg></div>
  </section>
  <div class="library-popup">Music library</div>
  <svg class="pointer" style="left:590px;top:1499px"><use href="#icon-pointer"/></svg>
  <svg class="pointer" style="left:872px;top:1539px"><use href="#icon-pointer"/></svg>
  <svg class="pointer" style="left:787px;top:1704px"><use href="#icon-pointer"/></svg>

  <!-- Alert pad -->
  <section class="pad pad--red" style="left:1058px;top:1270px">
    <div class="pad-id">AB1</div>
    <svg class="pad-close"><use href="#icon-close"/></svg>
    <div class="col-head col-head--status">Status</div>
    <div class="col-head col-head--event">ATC Event</div>
    <div class="pad-btn col-status small dim" style="top:173px;height:47px">Information</div>
    <div class="pad-btn col-status small dim" style="top:227px;height:44px">Caution</div>
    <div class="pad-btn col-status selected" style="top:277px;height:92px">Alert</div>
    <div class="pad-btn col-status notes" style="top:380px;height:87px">Notes</div>
    <div class="pad-btn col-event small dim" style="top:173px;height:47px">Landing</div>
    <div class="pad-btn col-event selected" style="top:225px;height:92px">Departure</div>
    <div class="pad-btn col-event small dim" style="top:325px;height:44px">Moon</div>
    <div class="pad-btn track small" style="top:380px;height:87px">Aria....</div>
    <div class="pad-btn music" style="top:380px;height:87px"><svg class="music-icon"><use href="#icon-staff"/></svg></div>
  </section>
</main>
</body>
</html>
```